Bright Meadow Counseling Business Card design with a visually interesting use of Space

I need business cards that are luxurious and give a peaceful, calm vibe. I also had some letterhead designed, and i like the look of it also, it's attached with the logo design for reference/ ideas but feel free to be creative.

Target Market(s)

High end luxurious client who needs counseling

Industry/Entity Type

Marriage and Family Therapy

Contact Information for Business Card

Mira Kowalczyk MS LMFT/ or Toby Hallett address 4150 Larkin Suite 600

Font styles to use
Sans Serif

Colors
0054AA
0677BA
7BADD7
CADEEF
E8F1F8
0094D4
00A9DD
6FCCEA
C7EBF8
E9F6FB
A7469A
B969AE
D3A5CF
EDDBEB
F8F0F9
6B429C
8869AF
B7A5CE
E3DAEB
F3F0F8

Requirements
Must have
• Logo and color scheme but be simple modern and luxurious
Nice to have
• I'd like to incorporate some elelmets from the logo and letterhead into a simple modern card

```html
<!DOCTYPE html>
<html lang="en">
<head>
<meta charset="utf-8">
<title>Bright Meadow Counseling – Business Card</title>
<link rel="stylesheet" href="https://fonts.googleapis.com/css2?family=Montserrat:wght@300;400&display=swap">
<style>
  :root {
    --backdrop: #d0d0d0;
    --card: #ffffff;
    --ink: #1c1c1c;
    --band: #e3d3e8;
    --plum: #b969ae;
    --lavender: #d9cdea;
  }
  * { margin: 0; padding: 0; box-sizing: border-box; }
  html, body {
    width: 1200px; height: 1101px; overflow: hidden;
    background: var(--backdrop);
    font-family: "Montserrat", sans-serif;
    color: var(--ink);
  }
  .stage { position: relative; width: 1200px; height: 1101px; }
  .card {
    position: absolute; top: 264px;
    width: 308px; height: 541px;
    background: var(--card);
  }
  .card--front { left: 243px; }
  .card--back { left: 640px; }

  /* front */
  .url-band {
    position: absolute; left: 143px; top: 123px;
    width: 22px; height: 209px;
    background: var(--band);
  }
  .url-band__text {
    position: absolute; left: 50%; top: 50%;
    transform: translate(-50%, -50%) rotate(-90deg);
    white-space: nowrap;
    font-size: 14px; font-weight: 400; letter-spacing: 0.3px;
  }
  .brand {
    position: absolute; right: 86px; top: 445px;
    text-align: right; font-weight: 300; color: var(--ink);
  }
  .brand__name { font-size: 24px; line-height: 1; }
  .brand__sub { font-size: 13px; letter-spacing: 2px; margin-top: 4px; }
  .brand__dot {
    position: absolute; left: 222px; top: 410px;
    width: 34px; height: 34px; border-radius: 50%;
    background: var(--plum);
  }

  /* back */
  .person {
    position: absolute; right: 38px; top: 60px;
    text-align: right; font-weight: 400;
  }
  .person__name { font-size: 22px; line-height: 1.1; }
  .person__role { font-size: 20px; line-height: 1.1; }
  .calm-mark {
    position: absolute; left: 60px; top: 130px;
    width: 210px; height: 210px;
  }
  .contact {
    position: absolute; left: 40px; top: 362px;
    list-style: none; font-size: 14.5px;
  }
  .contact__item { display: flex; align-items: center; height: 21.5px; }
  .contact__icon { width: 15px; height: 13px; margin-right: 8px; fill: var(--ink); }
  .address {
    position: absolute; left: 40px; top: 447px;
    font-size: 14.5px; line-height: 21.5px; font-style: normal;
  }
</style>
</head>
<body>
<main class="stage">
  <section class="card card--front" aria-label="Card front">
    <div class="url-band"><span class="url-band__text">www.brightmeadow.com</span></div>
    <span class="brand__dot" aria-hidden="true"></span>
    <div class="brand">
      <div class="brand__name">Bright Meadow</div>
      <div class="brand__sub">Counseling</div>
    </div>
  </section>

  <section class="card card--back" aria-label="Card back">
    <div class="person">
      <div class="person__name">Mira Kowalczyk</div>
      <div class="person__role">owner</div>
    </div>
    <svg class="calm-mark" viewBox="0 0 210 210" role="img" aria-label="Soft pastel brand motif">
      <circle cx="105" cy="105" r="100" fill="var(--lavender)" opacity="0.75"/>
    </svg>
    <ul class="contact">
      <li class="contact__item">
        <svg class="contact__icon" viewBox="0 0 16 14" aria-hidden="true"><path d="M1 4c0-2 3-3 7-3s7 1 7 3v1.5h-3.5V4h-7v1.5H1z"/><path d="M4 7l2-2h4l2 2v6H4z"/><circle cx="8" cy="9.5" r="1.6" fill="#fff"/></svg>
        482 - 617 - 3094
      </li>
      <li class="contact__item">
        <svg class="contact__icon" viewBox="0 0 16 14" aria-hidden="true"><path d="M4 0h7l1 1v3H4z"/><path d="M1 5h14v6h-3v3H4v-3H1z"/><rect x="5" y="9" width="6" height="3.5" fill="#fff"/></svg>
        482 - 617 - 3095
      </li>
      <li class="contact__item">
        <svg class="contact__icon" viewBox="0 0 16 14" aria-hidden="true"><path d="M0 2h16v10H0z"/><path d="M1 3l7 5 7-5M1 11l5-4M15 11l-5-4" stroke="#fff" stroke-width="1.2" fill="none"/></svg>
        info@brightmeadow.com
      </li>
    </ul>
    <address class="address">
      2214 Willow Crest Lane<br>
      Juneau, Alaska 99801
    </address>
  </section>
</main>
</body>
</html>
```